Build an Extreme sport website for Ridge Thrust Events Website

Platform: The website must be designed and developed using Webflow.
Pages:
Home Page:
Bold and high-impact design that reflects the extreme motorsport vibe.
Features an engaging hero section with high-quality imagery/videos.
Include sections for company highlights, key events, and sponsor logos.
Event Calendar Page:
Dynamic calendar showcasing upcoming events with dates, descriptions, and links for more details.
Sponsors Page:
Highlight our sponsors with logos, descriptions, and links to their websites.
Include a section for "How to Become a Sponsor."
Gallery/Media Page (Optional):
Showcase action-packed photos and videos from past events.
Contact Page:
Simple form for inquiries with fields for name, email, phone, and message.
Include links to social media and our physical address (if applicable).
Design Style:

Bold, trendy, and modern.
Incorporate vibrant colors and typography reflecting extreme motorsports.
High-quality visuals and media to convey energy and excitement.
Technical Features:

Fully responsive and mobile-optimized.
Easy-to-update CMS for event details, sponsor information, and media.
SEO-optimized design.
Target Audience:

Motorsports enthusiasts, sponsors, and event organizers.
References:

Use our our feed page @ridgethrustgarage for branding inspiration.
Design should align with the high-energy, extreme motorsport aesthetic we showcase there.
Deliverables:

Fully functioning Webflow website with all pages and features outlined above.
Any graphic assets used in the design.

Target Market(s)

Side Show / Drifting / Extreme car drivers

Number of Pages Required

4 page

Font styles to use
Sans Serif

Requirements
Nice to have
• Bold, trendy, and modern. Incorporate vibrant colors and typography reflecting extreme motorsports. High-quality visuals and media to convey energy and excitement.

```html
<!DOCTYPE html>
<html lang="en">
<head>
<meta charset="utf-8">
<title>Ridge Thrust Events</title>
<link href="https://fonts.googleapis.com/css2?family=Krona+One&family=Outfit:wght@400;500;600;700&family=Roboto:wght@400&display=swap" rel="stylesheet">
<style>
:root{
  --red:#e4002b;
  --red-deep:#9c0018;
  --ink:#231f20;
  --ink-2:#2b2728;
  --grey:#4a4546;
  --silver:#c9c9c9;
  --white:#ffffff;
  --text-soft:#d8d8d8;
  --display:"Krona One", sans-serif;
  --body:"Outfit", sans-serif;
}
*{box-sizing:border-box;margin:0;padding:0}
html,body{width:1200px;height:3703px;overflow:hidden;background:var(--ink)}
body{font-family:var(--body);color:var(--white)}
.page{position:relative;width:1200px;height:3703px;overflow:hidden;background:var(--ink)}
.abs{position:absolute}
.brand{display:flex;align-items:center;gap:10px;font-family:var(--body);font-weight:700;color:var(--white);text-transform:uppercase;letter-spacing:.5px}
.brand-square{width:18px;height:18px;background:var(--red);flex:none}
a{color:inherit;text-decoration:none}
.btn{display:flex;align-items:center;justify-content:center;border-radius:30px;font-family:var(--body);font-weight:600;font-size:14px;text-transform:uppercase;color:var(--white)}
.btn-red{background:var(--red)}
.btn-outline{border:2px solid var(--white);background:rgba(35,31,32,.6)}
.section-title{font-family:var(--display);font-size:38px;text-transform:uppercase;text-align:center;letter-spacing:1px;line-height:1}
.section-title .hl{color:var(--red)}

/* nav */
.nav-link{position:absolute;top:34px;font-size:15px;font-weight:600;text-transform:uppercase}
.nav-home{position:absolute;left:561px;top:10px;width:72px;height:72px;border-radius:50%;background:var(--red);display:flex;align-items:center;justify-content:center;font-weight:600;font-size:15px;text-transform:uppercase}

/* hero */
.hero-media{left:0;top:0;width:1200px;height:660px;background:
  radial-gradient(ellipse at 45% 60%,rgba(200,30,40,.55),transparent 40%),
  radial-gradient(ellipse at 85% 45%,rgba(190,160,40,.35),transparent 30%),
  linear-gradient(180deg,#5d5a58 0%,#7a7775 35%,#4b4847 70%,#2e2b2b 100%)}
.hero-shade{left:0;top:0;width:1200px;height:120px;background:linear-gradient(180deg,rgba(35,31,32,.95),rgba(35,31,32,0))}
.hero-title{left:0;width:1200px;text-align:center;font-family:var(--display);font-size:44px;line-height:1;text-transform:uppercase}
.hero-sub{left:0;top:333px;width:1200px;text-align:center;font-size:19px}
.play{left:1110px;top:537px;width:42px;height:42px;border-radius:50%;background:var(--white);display:flex;align-items:center;justify-content:center}

/* about */
.about-title{left:622px;top:690px;font-family:var(--display);font-size:36px;text-transform:uppercase}
.about-sub{left:621px;top:741px;font-size:19px}
.about-text{left:621px;top:786px;width:423px;font-size:13.5px;line-height:24px;text-align:justify;color:var(--text-soft)}

/* events */
.card{position:absolute;top:1358px;width:256px;height:335px;background:var(--white);overflow:hidden}
.card-media{position:absolute;left:0;top:0;width:256px;height:182px}
.card-panel{position:absolute;left:0;top:160px;width:256px;height:175px;background:var(--white);clip-path:polygon(0 14%,0 100%,100% 100%,100% 0)}
.card-edge{position:absolute;left:0;top:150px;width:256px;height:185px;background:var(--red);clip-path:polygon(0 20%,3% 16%,3% 92%,18% 97%,0 100%)}
.card-title{position:absolute;left:36px;top:205px;width:200px;font-size:13px;font-weight:600;color:#1a1a1a;text-transform:uppercase;line-height:16px}
.card-text{position:absolute;left:36px;top:246px;width:200px;font-size:12.5px;color:#555;line-height:17px}
.card-date{position:absolute;left:50px;top:301px;font-size:11px;color:#222;display:flex;align-items:center;gap:6px}
.card-btn{position:absolute;left:148px;top:294px;width:94px;height:28px;border-radius:14px;font-size:10.5px}
.btn-dark{background:#4a4546}
.slider-arrow{position:absolute;width:44px;height:44px;border-radius:50%;border:2px solid var(--white);background:rgba(35,31,32,.4);display:flex;align-items:center;justify-content:center}

/* sponsors */
.sponsor{position:absolute;top:2148px;height:102px;border-radius:51px;background:#111;border:2px solid #333;display:flex;align-items:center;justify-content:center;font-family:var(--body);font-weight:700;font-size:17px;text-transform:uppercase;color:var(--white)}
.sponsor.active{border-color:var(--red);background:#1a1516}

/* contact */
.field{position:absolute;background:var(--white);border:none;font-family:"Roboto",sans-serif;font-size:15px;color:#666;padding:0 21px;display:flex;align-items:center}
.field.area{align-items:flex-start;padding-top:16px}

/* follow */
.insta{position:absolute;top:3171px;width:223px;height:186px}

/* footer */
.foot-link{position:absolute;top:3531px;font-size:16px;font-weight:600;text-transform:uppercase}
.social{position:absolute;top:3610px;width:32px;height:32px;border-radius:50%;background:#e6e6e6}
</style>
</head>
<body>
<div class="page">

  <!-- HERO -->
  <header>
    <div class="abs hero-media" role="img" aria-label="Open-wheel race cars lined up on a track, red car in front"></div>
    <div class="abs hero-shade"></div>
    <div class="abs" style="left:0;top:0;width:1200px;height:5px;background:var(--red)"></div>
    <a class="abs brand" href="#" style="left:150px;top:78px;font-size:19px"><span class="brand-square"></span>Ridge Thrust Events</a>
    <nav>
      <a class="nav-home" href="#">Home</a>
      <a class="nav-link" href="#" style="left:659px">Events</a>
      <a class="nav-link" href="#" style="left:756px">Sponsors</a>
      <a class="nav-link" href="#" style="left:878px">Gallery</a>
      <a class="nav-link" href="#" style="left:984px">Contact</a>
    </nav>
    <h1>
      <span class="abs hero-title" style="top:213px">Fueling the Passion for</span>
      <span class="abs hero-title" style="top:267px;color:var(--red)">Extreme Motorsports</span>
    </h1>
    <p class="abs hero-sub">Connecting Motorsports Enthusiasts, Sponsors, and Event Organizers</p>
    <a class="abs btn btn-red" href="#" style="left:405px;top:391px;width:189px;height:56px;border:2px solid var(--white)">Explore Events</a>
    <a class="abs btn btn-outline" href="#" style="left:605px;top:391px;width:190px;height:56px">Become a Sponsor</a>
    <a class="abs play" href="#" aria-label="Play video"><svg width="16" height="18" viewBox="0 0 16 18"><path d="M2 1l13 8-13 8z" fill="var(--red)"/></svg></a>
  </header>

  <svg class="abs" style="left:0;top:540px" width="1200" height="130" viewBox="0 0 1200 130">
    <polygon points="0,118 611,14 1200,118 1200,130 0,130" fill="var(--ink)"/>
    <polyline points="0,118 611,14 1200,118" fill="none" stroke="var(--red)" stroke-width="8"/>
  </svg>

  <!-- ABOUT -->
  <section>
    <div class="abs" style="left:155px;top:690px;width:384px;height:338px;display:flex;align-items:center;justify-content:center">
      <div class="brand" style="font-size:30px"><span class="brand-square" style="width:28px;height:28px"></span>Ridge Thrust Events</div>
    </div>
    <h2 class="abs about-title">About <span style="color:var(--red)">Us</span></h2>
    <p class="abs about-sub">Experience the Thrill</p>
    <p class="abs about-text">Sed ut perspiciatis unde omnis iste natus error sit voluptatem accusantium doloremque laudantium, totam rem aperiam, eaque ipsa quae ab illo inventore veritatis et quasi architecto beatae vitae dicta sunt explicabo. Nemo enim ipsam voluptatem quia voluptas sit aspernatur aut odit aut fugit, sed quia consequuntur magni dolores eos qui ratione voluptatem sequi nescorro quiui dolorem ipsum quia dolor sit amet</p>
    <a class="abs btn btn-red" href="#" style="left:621px;top:981px;width:136px;height:43px;font-size:14px">Read More</a>
  </section>

  <!-- EVENTS -->
  <section>
    <svg class="abs" style="left:0;top:1110px" width="1200" height="900" viewBox="0 0 1200 900">
      <defs>
        <linearGradient id="evbg" x1="0" y1="0" x2="0" y2="1">
          <stop offset="0" stop-color="#4a4546"/><stop offset=".6" stop-color="#333031"/><stop offset="1" stop-color="#1d1a1b"/>
        </linearGradient>
        <linearGradient id="redv" x1="0" y1="0" x2="0" y2="1">
          <stop offset="0" stop-color="#ff1a3d"/><stop offset="1" stop-color="var(--red)"/>
        </linearGradient>
      </defs>
      <polygon points="0,176 600,4 1200,176 1200,672 600,866 0,672" fill="url(#evbg)"/>
      <polyline points="0,176 600,4 1200,176" fill="none" stroke="#b9b9b9" stroke-width="7"/>
      <polygon points="0,672 600,760 1200,672 1200,682 600,866 0,682" fill="url(#redv)"/>
    </svg>
    <div class="abs" role="img" aria-label="Checkered flags across a dark track" style="left:290px;top:1805px;width:620px;height:90px;background:linear-gradient(180deg,rgba(120,120,120,.35),rgba(60,60,60,.15));clip-path:polygon(0 0,100% 0,50% 100%)"></div>

    <h2 class="abs section-title" style="left:0;top:1262px;width:1200px">Upcoming <span class="hl">Events</span></h2>

    <div class="abs" style="left:148px;top:1343px;width:62px;height:36px;border-left:5px solid var(--red);border-top:5px solid var(--red)"></div>
    <div class="abs" style="left:990px;top:1673px;width:62px;height:36px;border-right:5px solid var(--red);border-bottom:5px solid var(--red)"></div>

    <article class="card" style="left:164px">
      <div class="card-media" role="img" aria-label="Red sports car on a race circuit under a cloudy sky" style="background:linear-gradient(180deg,#8e9296 0%,#bfb8b3 45%,#a33a3f 70%,#6d5f5c 100%)"></div>
      <div class="card-edge"></div><div class="card-panel"></div>
      <h3 class="card-title">Sed ut perspiciatis unde omnis iste nror sit</h3>
      <p class="card-text">Sed ut perspiciatis unde omnis iste natus error sit volupt</p>
      <span class="card-date"><svg width="11" height="11" viewBox="0 0 11 11"><rect x="1" y="2" width="9" height="8" fill="none" stroke="var(--red)" stroke-width="1.3"/><line x1="1" y1="4.5" x2="10" y2="4.5" stroke="var(--red)"/></svg>DEC 12,2024</span>
      <a class="card-btn btn btn-dark" href="#">Read More</a>
    </article>

    <article class="card" style="left:471px">
      <div class="card-media" role="img" aria-label="Car engine bay in red tint" style="background:linear-gradient(160deg,#b8001f 0%,#e4002b 50%,#8a0016 100%)"></div>
      <div class="abs" style="left:113px;top:100px;width:30px;height:30px;border-radius:50%;background:#231f20;border:2px solid #fff;display:flex;align-items:center;justify-content:center"><svg width="12" height="12" viewBox="0 0 12 12"><path d="M6 1v10M1 6h10" stroke="#fff" stroke-width="2"/></svg></div>
      <div class="card-edge"></div><div class="card-panel"></div>
      <h3 class="card-title">Sed ut perspiciatis unde omnis iste nror sit</h3>
      <p class="card-text">Sed ut perspiciatis unde omnis iste natus error sit volupt</p>
      <span class="card-date"><svg width="11" height="11" viewBox="0 0 11 11"><rect x="1" y="2" width="9" height="8" fill="none" stroke="var(--red)" stroke-width="1.3"/><line x1="1" y1="4.5" x2="10" y2="4.5" stroke="var(--red)"/></svg>DEC 12,2024</span>
      <a class="card-btn btn btn-red" href="#">Read More</a>
    </article>

    <article class="card" style="left:778px">
      <div class="card-media" role="img" aria-label="Orange muscle car doing a burnout in front of a crowd" style="background:linear-gradient(180deg,#cfd6de 0%,#6c7565 35%,#c98a3a 65%,#9a9a98 100%)"></div>
      <div class="card-edge"></div><div class="card-panel"></div>
      <h3 class="card-title">Sed ut perspiciatis unde omnis iste nror sit</h3>
      <p class="card-text">Sed ut perspiciatis unde omnis iste natus error sit volupt</p>
      <span class="card-date"><svg width="11" height="11" viewBox="0 0 11 11"><rect x="1" y="2" width="9" height="8" fill="none" stroke="var(--red)" stroke-width="1.3"/><line x1="1" y1="4.5" x2="10" y2="4.5" stroke="var(--red)"/></svg>DEC 12,2024</span>
      <a class="card-btn btn btn-dark" href="#">Read More</a>
    </article>

    <a class="slider-arrow" href="#" aria-label="Previous" style="left:72px;top:1509px"><svg width="12" height="18" viewBox="0 0 12 18"><path d="M10 2L3 9l7 7" fill="none" stroke="#fff" stroke-width="2.5"/></svg></a>
    <a class="slider-arrow" href="#" aria-label="Next" style="left:1083px;top:1509px"><svg width="12" height="18" viewBox="0 0 12 18"><path d="M2 2l7 7-7 7" fill="none" stroke="#fff" stroke-width="2.5"/></svg></a>

    <a class="abs btn btn-red" href="#" style="left:492px;top:1733px;width:217px;height:43px">Load More Events</a>
  </section>

  <!-- SPONSORS -->
  <section>
    <h2 class="abs section-title" style="left:0;top:2066px;width:1200px">Our <span class="hl">Sponsors</span></h2>
    <div class="sponsor" style="left:145px;width:214px">Apex Line</div>
    <div class="sponsor" style="left:377px;width:212px">Torque Union</div>
    <div class="sponsor active" style="left:608px;width:216px">Burnout Co.</div>
    <div class="sponsor" style="left:839px;width:215px">Redline Works</div>
    <a class="slider-arrow" href="#" aria-label="Previous" style="left:72px;top:2179px"><svg width="12" height="18" viewBox="0 0 12 18"><path d="M10 2L3 9l7 7" fill="none" stroke="#fff" stroke-width="2.5"/></svg></a>
    <a class="slider-arrow" href="#" aria-label="Next" style="left:1083px;top:2179px"><svg width="12" height="18" viewBox="0 0 12 18"><path d="M2 2l7 7-7 7" fill="none" stroke="#fff" stroke-width="2.5"/></svg></a>
  </section>

  <!-- CONTACT -->
  <section>
    <svg class="abs" style="left:0;top:2300px" width="1200" height="790" viewBox="0 0 1200 790">
      <defs>
        <radialGradient id="ctbg" cx=".5" cy=".55" r=".7">
          <stop offset="0" stop-color="#d0102e"/><stop offset=".6" stop-color="#8e0a1e"/><stop offset="1" stop-color="#5a0613"/>
        </radialGradient>
      </defs>
      <rect x="0" y="7" width="1200" height="783" fill="url(#ctbg)"/>
      <polygon points="0,0 1200,0 1200,28 600,115 0,28" fill="var(--ink)"/>
      <polyline points="120,30 600,108 1080,30" fill="none" stroke="#bdbdbd" stroke-width="6"/>
      <polygon points="0,780 600,673 1200,780 1200,790 0,790" fill="var(--ink)"/>
      <polyline points="0,780 600,673 1200,780" fill="none" stroke="#bdbdbd" stroke-width="6"/>
    </svg>
    <div class="abs" role="img" aria-label="Red stage lights glowing" style="left:230px;top:2360px;width:740px;height:60px;background:radial-gradient(ellipse at center,rgba(255,60,80,.45),transparent 70%)"></div>

    <h2 class="abs section-title" style="left:0;top:2496px;width:1200px">Contact Us</h2>
    <form>
      <div class="field" style="left:234px;top:2573px;width:360px;height:53px">First Name</div>
      <div class="field" style="left:605px;top:2573px;width:360px;height:53px">Last Name</div>
      <div class="field" style="left:234px;top:2638px;width:360px;height:53px">Email address</div>
      <div class="field" style="left:605px;top:2638px;width:360px;height:53px">Phone Number</div>
      <div class="field area" style="left:234px;top:2703px;width:731px;height:114px">Message</div>
      <a class="abs btn" href="#" style="left:505px;top:2847px;width:191px;height:42px;background:var(--ink)">Submit Message</a>
    </form>
  </section>

  <!-- FOLLOW -->
  <section>
    <div class="abs" style="left:0;top:3091px;width:1200px;display:flex;justify-content:center;align-items:center;gap:16px">
      <span style="width:28px;height:28px;background:var(--red);display:block"></span>
      <h2 class="section-title">Follow <span class="hl">Us</span></h2>
    </div>
    <div class="insta" role="img" aria-label="Silver muscle car drifting at a car meet" style="left:144px;background:linear-gradient(180deg,#9aa39a 0%,#6e7366 40%,#8d8f92 70%,#5b5c5e 100%)"></div>
    <div class="insta" role="img" aria-label="Black classic car on chrome wheels" style="left:374px;background:linear-gradient(160deg,#3a3a3c 0%,#111 55%,#55565a 100%)"></div>
    <div class="abs" style="left:474px;top:3252px;width:24px;height:24px;border-radius:50%;background:var(--red)"></div>
    <div class="insta" role="img" aria-label="Car burnout with smoke surrounded by spectators" style="left:604px;background:linear-gradient(170deg,#7a6a4c 0%,#b9ab90 45%,#8b7a5a 100%)"></div>
    <div class="insta" role="img" aria-label="Glossy black car under blue sky" style="left:834px;background:linear-gradient(160deg,#2f5fb8 0%,#1d2e5c 40%,#0d0d10 75%,#2a2520 100%)"></div>
    <a class="abs" href="#" style="left:0;top:3384px;width:1200px;display:flex;justify-content:center;align-items:center;gap:8px;font-size:16px;text-decoration:underline;text-transform:uppercase">
      <span style="width:12px;height:12px;background:var(--red);display:block"></span>Follow us on our feed
    </a>
  </section>

  <!-- FOOTER -->
  <footer>
    <div class="abs" style="left:0;top:3462px;width:1200px;height:4px;background:var(--red)"></div>
    <div class="abs brand" style="left:170px;top:3570px;font-size:17px"><span class="brand-square"></span>Ridge Thrust Events</div>
    <a class="foot-link" href="#" style="left:461px">Home</a>
    <a class="foot-link" href="#" style="left:549px">Events</a>
    <a class="foot-link" href="#" style="left:653px">Sponsors</a>
    <a class="foot-link" href="#" style="left:781px">Gallery</a>
    <a class="foot-link" href="#" style="left:893px">Contact</a>
    <p class="abs" style="left:461px;top:3569px;font-size:13px;color:var(--text-soft)">© 2024 Ridge Thrust Events.All Rights Reserved &nbsp;| &nbsp;Privacy Policy &nbsp;| &nbsp;Terms of use</p>
    <a class="social" href="#" aria-label="Social profile one" style="left:462px"></a>
    <a class="social" href="#" aria-label="Social profile two" style="left:502px;background:var(--red)"></a>
    <a class="social" href="#" aria-label="Social profile three" style="left:542px"></a>
  </footer>

</div>
</body>
</html>
```